Australian Export Wine Label

Brand

To design a label based around Australia’s famous bush ranger Tom Brody called Brody’s Hollow.

Imagery for the label could be an abstract image of Tom’s armour of even of himself or we are open to other possibilities ranging from a traditional label to a more contemporary look and feel.

Images should not include guns and imagery used must be free of copyright.

Designs should be able to be printed by the standard 4 colour print process. As this is not an expensive product there will be no expensive label fiunishes such as gold foil or embossing

The range

The range of wines will consist of a 2011 Shiraz, 2012 Sauvignon Blanc and 2011 Chardonnay.

Market

The primary market for these wines is Ireland with the price range being in the $10-15 bracket. The wines will be available in independent retail shops and restaurants

Front Label Mandatories

1. Front Label: should not exceed 110mm x 80mm

2. Brand name - Brody’s Hollow

3. Vintage & Variety – for example 2011 Shiraz

4. Origin – Wine of Australia

5. Text to appear on front label: Born in Co. Antrim, the remarkable Martha Brody had eight children including Australia’s most famous Bushranger Tom Brody. The family’s wild and independent spirit is legendary in country Australia.

Back Label Mandatories

1. Back Label: 80mm x 80mm

2. Brand name

3. Vintage & Variety

4. Alcohol, Volume, Country of production

5. 13.0% VOL 750Ml (must be 4mm in height)

6. Contains egg, milk and nuts. Traces may remain

7. Please include the pregnant lady logo and a recycling logo

8. Wine of Australia

9. Space for barcode

10. Text to appear on back label (Shiraz):

Brody’s Hollow is our vineyard named after the Brody family, whose homestead stood here long before the vines were planted.
Our Brody’s Hollow Shiraz is bold and full of flavour. Plums, cassis, chocolate and spice intermingle on the nose and palate, resulting in a full bodied, vibrant wine. Enjoy with a spirit of adventure and a hearty beef stew.

```html
<!DOCTYPE html>
<html lang="en">
<head>
<meta charset="utf-8">
<title>Brody’s Hollow Shiraz 2011 — Front Label</title>
<link rel="stylesheet" href="https://fonts.googleapis.com/css2?family=Libre+Baskerville:wght@400;700&family=Special+Elite&family=Pinyon+Script&display=swap">
<style>
  :root {
    --backdrop: #1b1b1d;
    --paper: #f6f5f1;
    --paper-edge: #e6e4de;
    --ink: #141414;
    --wine-red: #a3122a;
    --rule: #6d6d6d;
    --origin-ink: #3a3a3a;
    --story-ink: #2a2a2a;
    --art-dark: #3a3a3a;
    --art-mid: #8a8a86;
    --art-light: #d9d8d3;
  }
  * { box-sizing: border-box; margin: 0; padding: 0; }
  html, body {
    width: 1094px;
    height: 1200px;
    overflow: hidden;
    background: var(--backdrop);
  }
  .canvas {
    width: 1094px;
    height: 1200px;
    display: flex;
    align-items: center;
    justify-content: center;
  }
  .label {
    width: 800px;
    height: 1040px;
    background: radial-gradient(ellipse at 40% 30%, var(--paper) 60%, var(--paper-edge) 100%);
    border-radius: 6px;
    display: flex;
    flex-direction: column;
    align-items: center;
    padding-top: 70px;
    color: var(--ink);
  }
  .label__artwork {
    width: 280px;
    height: 250px;
    border-radius: 4px;
    background: radial-gradient(ellipse at 50% 45%, var(--art-dark) 0%, var(--art-mid) 55%, var(--art-light) 100%);
  }
  .label__brand {
    margin-top: 60px;
    font-family: "Libre Baskerville", Georgia, serif;
    font-weight: 700;
    font-size: 66px;
    letter-spacing: 1px;
    line-height: 1;
    white-space: nowrap;
  }
  .label__variety {
    margin-top: 34px;
    display: flex;
    align-items: center;
    gap: 14px;
    font-family: "Libre Baskerville", Georgia, serif;
    font-size: 40px;
    color: var(--wine-red);
    letter-spacing: 1px;
  }
  .label__variety::before,
  .label__variety::after {
    content: "";
    display: block;
    width: 50px;
    height: 2px;
    background: var(--ink);
  }
  .label__vintage {
    margin-top: 6px;
    font-family: "Libre Baskerville", Georgia, serif;
    font-size: 46px;
    color: var(--wine-red);
    letter-spacing: 2px;
  }
  .label__flourish {
    margin-top: 34px;
    width: 230px;
    height: 70px;
    border-radius: 4px;
    background: linear-gradient(180deg, var(--art-dark), var(--art-mid));
  }
  .label__origin {
    margin-top: 50px;
    width: 640px;
    border-top: 2px solid var(--rule);
    padding-top: 16px;
    padding-left: 110px;
    font-family: "Special Elite", "Courier New", monospace;
    font-size: 32px;
    letter-spacing: 4px;
    color: var(--origin-ink);
  }
  .label__story {
    margin-top: 26px;
    width: 690px;
    font-family: "Pinyon Script", cursive;
    font-size: 25px;
    line-height: 1.5;
    text-align: center;
    color: var(--story-ink);
  }
</style>
</head>
<body>
  <main class="canvas">
    <article class="label">
      <div class="label__artwork" role="img" aria-label="Ink illustration of the bushranger’s iron helmet standing on a patch of scrubby ground"></div>

      <h1 class="label__brand">BRODY’S HOLLOW</h1>
      <p class="label__variety">SHIRAZ</p>
      <p class="label__vintage">2011</p>

      <div class="label__flourish" role="img" aria-label="Decorative black scroll ornament"></div>

      <p class="label__origin">Wine of Australia</p>

      <p class="label__story">
        Born in Co. Antrim, the remarkable Martha Brody had eight children including
        Australia’s most famous Bushranger Tom Brody. The family’s wild and
        independent spirit is legendary in country Australia.
      </p>
    </article>
  </main>
</body>
</html>
```